Hawaiian skin care product needs label design

We are looking for a font for Hawaiian skin care product called 'omu - which means 'skin' in Hawaiian.
No need for a logo or a mark, simply looking for a clean, fresh, modern, young, and crisp font and background for our product label.
We are creating the label for the product bag, see file attached for reference.
Ideas we like: Subtle gradient water color back ground, fade chevron, see files attached.
This is a women's product, but don't want it to be too feminine or overly girly. Fresh and crisp, modern with subtle undertones of femininity.
Updates

Reason: Need to have the back of the label created as well.

Target Market(s)

Women, ages 18-40 Up scale, modern, hip. Mature and sophisticated.

Industry/Entity Type

Skin Care Product

Logo Text

'omu

Logo styles of interest
Wordmark Logo
Font styles to use
Sans Serif

Requirements
Must have
• This is for a label on a bag, attached images below to show our bag, pouch. We are not sure which color to go with as of yet.
Should not have
• No logo, no need for a mark of any kind.
Not childish or overly girly.

```html
<!DOCTYPE html>
<html lang="en">
<head>
<meta charset="utf-8">
<title>'omu — Body Scrub Label</title>
<link href="https://fonts.googleapis.com/css2?family=Josefin+Sans:wght@400;600&family=Josefin+Slab:wght@700&family=Courier+Prime&display=swap" rel="stylesheet">
<style>
  :root {
    --page: #ffffff;
    --label: #ffffff;
    --ink: #2a2a2a;
    --peach: #efcdb8;
    --sand: #f3e3d2;
    --mist: #d6e6e6;
    --caption: #222222;
    --edge: #f0f0f0;
  }
  * { margin: 0; padding: 0; box-sizing: border-box; }
  html, body { width: 1200px; height: 1000px; overflow: hidden; background: var(--page); }
  .canvas { position: relative; width: 1200px; height: 1000px; }

  .label {
    position: absolute;
    top: 220px;
    width: 282px;
    height: 330px;
    background: var(--label);
    box-shadow: 0 0 0 1px var(--edge);
    overflow: hidden;
  }
  .label--caps { left: 211px; }
  .label--lower { left: 717px; }

  .pattern-band {
    position: absolute;
    left: 10px;
    right: 10px;
  }
  .pattern-band--top {
    top: 8px;
    height: 50px;
    background: linear-gradient(180deg, var(--peach) 0%, var(--sand) 100%);
    opacity: 0.8;
  }
  .pattern-band--lower {
    top: 134px;
    height: 188px;
    background: linear-gradient(180deg, var(--sand) 0%, var(--mist) 25%, var(--peach) 45%, var(--sand) 62%, var(--mist) 80%, var(--peach) 100%);
    opacity: 0.6;
  }

  .copy {
    position: absolute;
    left: 0;
    right: 0;
    text-align: center;
    color: var(--ink);
  }
  .brand-name {
    top: 84px;
    font-family: "Josefin Sans", sans-serif;
    font-weight: 600;
    font-size: 22px;
    letter-spacing: 2px;
  }
  .range {
    top: 153px;
    font-family: "Josefin Sans", sans-serif;
    font-weight: 600;
    font-size: 12px;
    letter-spacing: 1.2px;
  }
  .product {
    top: 180px;
    font-family: "Josefin Slab", serif;
    font-weight: 700;
    font-size: 28px;
    letter-spacing: 2.6px;
  }
  .variant {
    top: 229px;
    font-family: "Josefin Sans", sans-serif;
    font-weight: 600;
    font-size: 11.5px;
    letter-spacing: 1.2px;
  }
  .weight {
    top: 297px;
    font-family: "Josefin Sans", sans-serif;
    font-weight: 600;
    font-size: 11px;
    letter-spacing: 1px;
  }

  .caption {
    position: absolute;
    left: 691px;
    top: 799px;
    font-family: "Courier Prime", monospace;
    font-size: 10px;
    color: var(--caption);
  }
</style>
</head>
<body>
<main class="canvas">

  <section class="label label--caps">
    <div class="pattern-band pattern-band--top" role="img" aria-label="Faded peach and sand chevron pattern"></div>
    <div class="pattern-band pattern-band--lower" role="img" aria-label="Faded peach, sand and mist blue chevron pattern"></div>
    <p class="copy brand-name">'OMU</p>
    <p class="copy range">HAWAIIN SKINCARE</p>
    <h1 class="copy product">BODY SCRUB</h1>
    <p class="copy variant">SEA SALT &amp; COCONUT</p>
    <p class="copy weight">500gm</p>
  </section>

  <section class="label label--lower">
    <div class="pattern-band pattern-band--top" role="img" aria-label="Faded peach and sand chevron pattern"></div>
    <div class="pattern-band pattern-band--lower" role="img" aria-label="Faded peach, sand and mist blue chevron pattern"></div>
    <p class="copy brand-name">'omu</p>
    <p class="copy range">HAWAIIN SKINCARE</p>
    <h2 class="copy product">BODY SCRUB</h2>
    <p class="copy variant">SEA SALT &amp; COCONUT</p>
    <p class="copy weight">500gm</p>
  </section>

  <p class="caption">lowercase logotype</p>

</main>
</body>
</html>
```